We need a business card design for our residential home building company based out of East Tennessee and the Smoky Mountains. We have 30 years of experience, and we plan to build homes not only in the state of Tennessee, but out of state as well. We are a different kind of production home builder; we aim to build homes cost-effectively and efficiently but with the character, dignity, and charm of historic homes. Our homes have a timeless style with modern floorplans and features. We would like to see designs that embody a classic style with accents of gold, red, and blue. The resulting business card should convey elegance, strength, character, and trust as well as the careful balance of the old and new.
Motto: "Shaping Lasting Roots"
Reason: I would like to extend the deadline so that more changes can be made to the best designs.
Target Market(s)
Adults 40+ from the Northern states looking to settle in Tennessee.
Industry/Entity Type
Residential
Contact Information for Business Card
Birchwood Dwellworks, LLC
Marla Pettigrew | Director of Operations
20815 Thornbury Lane | Suite 300
Knoxville, TN 37091
Office: (865)413-2958
Mobile: (865)690-8142
Email: marla@birchwooddwellworks.example

```html
<!DOCTYPE html>
<html lang="en">
<head>
<meta charset="utf-8">
<title>Birchwood Dwellworks, LLC — Business Card</title>
<link rel="stylesheet" href="https://fonts.googleapis.com/css2?family=Archivo+Narrow:wght@700&family=Arimo:wght@700&family=Cormorant+Garamond:ital,wght@0,700;1,500&display=swap">
<style>
  :root {
    --page: #e9e9e9;
    --cream: #fbeea0;
    --cream-light: #fdf5c4;
    --red: #ee1111;
    --red-deep: #c80000;
    --gold: #d9a21a;
    --gold-dark: #a87410;
    --olive: #6b5a2e;
    --navy: #1c2a7a;
    --ink: #141414;
    --white: #ffffff;
    --title-cream: #fff4b8;
  }
  * { margin: 0; padding: 0; box-sizing: border-box; }
  html, body { width: 1200px; height: 1200px; overflow: hidden; }
  body { position: relative; background: var(--page); }

  .card {
    position: absolute;
    width: 596px; height: 338px;
    background: linear-gradient(180deg, var(--cream-light), var(--cream));
    box-shadow: 6px 8px 10px rgba(0,0,0,.55);
    overflow: hidden;
  }
  .card svg { position: absolute; inset: 0; }
  .card--front { left: 74px; top: 134px; }
  .card--back { left: 526px; top: 722px; }

  .side-label {
    position: absolute;
    width: 504px;
    display: flex; align-items: center; justify-content: center;
    font-family: "Archivo Narrow", sans-serif;
    font-weight: 700; font-size: 84px; color: var(--ink);
    letter-spacing: 2px;
    background: linear-gradient(90deg, var(--cream) 0%, #fdf3c0 45%, var(--white) 100%);
  }
  .side-label--front { left: 696px; top: 214px; height: 178px; }
  .side-label--back { left: 0; top: 804px; height: 174px; }

  .tagline {
    position: absolute; left: 0; right: 0; top: 10px;
    text-align: center;
    font-family: "Cormorant Garamond", serif;
    font-style: italic; font-weight: 500;
    font-size: 28px; letter-spacing: 4px;
    color: var(--olive);
  }
  .front-name {
    position: absolute; left: 176px; top: 120px; width: 244px;
    text-align: center;
    font-family: "Cormorant Garamond", serif;
    font-weight: 700; font-size: 30px; line-height: 1.05;
    color: var(--gold-dark);
  }
  .flourish {
    position: absolute; left: 184px; top: 314px; width: 228px; height: 12px;
    border-radius: 6px;
    background: linear-gradient(90deg, #f1d0a0, #d7a35e 50%, #b8c6e0);
  }

  .person {
    position: absolute; left: 0; top: 148px; width: 240px;
    text-align: right;
    font-family: "Arimo", sans-serif; font-weight: 700;
  }
  .person__name {
    font-size: 25px; font-variant: small-caps; color: var(--navy); line-height: 1;
  }
  .person__title {
    font-size: 11px; text-transform: uppercase; color: var(--title-cream);
    margin-top: 3px; letter-spacing: .3px;
  }
  .back-name {
    position: absolute; left: 400px; top: 40px; width: 170px;
    text-align: center;
    font-family: "Cormorant Garamond", serif;
    font-weight: 700; font-size: 24px; line-height: 1.05;
    color: var(--gold);
  }
  .contact {
    position: absolute; right: 13px; top: 218px;
    list-style: none; text-align: right;
    font-family: "Archivo Narrow", sans-serif; font-weight: 700;
    font-size: 16px; line-height: 22px; color: var(--white);
  }
  .contact .tight { line-height: 19px; }
</style>
</head>
<body>

  <section class="card card--front" aria-label="Business card front">
    <svg width="596" height="338" viewBox="0 0 596 338">
      <defs>
        <linearGradient id="band" x1="0" x2="0" y1="0" y2="1">
          <stop offset="0" stop-color="#ff2a1a"/>
          <stop offset="1" stop-color="#e00000"/>
        </linearGradient>
        <radialGradient id="medallion" cx="0.5" cy="0.45" r="0.6">
          <stop offset="0" stop-color="#fef8d0"/>
          <stop offset="1" stop-color="#f7e07a"/>
        </radialGradient>
      </defs>
      <rect class="card-band" x="0" y="118" width="596" height="104" fill="url(#band)"/>
      <rect x="0" y="222" width="596" height="6" fill="rgba(0,0,0,.18)"/>
      <ellipse class="medallion" cx="298" cy="168" rx="130" ry="115" fill="url(#medallion)" stroke="var(--gold)" stroke-width="8"/>
      <ellipse cx="298" cy="168" rx="124" ry="109" fill="none" stroke="#f4cc4a" stroke-width="2"/>
    </svg>
    <p class="tagline">Shaping Lasting Roots</p>
    <p class="front-name">Birchwood Dwellworks, LLC</p>
    <div class="flourish" role="img" aria-label="Decorative scroll flourish in red, gold and blue"></div>
  </section>

  <div class="side-label side-label--front">FRONT</div>

  <div class="side-label side-label--back">BACK</div>

  <section class="card card--back" aria-label="Business card back">
    <svg width="596" height="338" viewBox="0 0 596 338">
      <defs>
        <linearGradient id="panel" x1="0" x2="1" y1="0" y2="0">
          <stop offset="0" stop-color="#d80000"/>
          <stop offset="1" stop-color="#ff1010"/>
        </linearGradient>
      </defs>
      <path class="red-panel" d="M302,0 C344,90 352,230 298,338 L596,338 L596,0 Z" fill="url(#panel)" stroke="#8a5a10" stroke-width="2"/>
      <path d="M0,124 L281,124 L262,175 L281,226 L0,226 Z" fill="rgba(0,0,0,.25)"/>
      <path class="name-ribbon" d="M0,118 L281,118 L262,169 L281,220 L0,220 Z" fill="var(--red)"/>
    </svg>
    <div class="person">
      <p class="person__name">Marla Pettigrew</p>
      <p class="person__title">Director of Operations</p>
    </div>
    <p class="back-name">Birchwood Dwellworks, LLC</p>
    <ul class="contact">
      <li>Office: (865)413-2958</li>
      <li>Mobile: (865)690-8142</li>
      <li class="tight">20815 Thornbury Lane &nbsp;Suite 300</li>
      <li class="tight">Knoxville, TN 37091</li>
      <li class="tight">marla@birchwooddwellworks.example</li>
    </ul>
  </section>

</body>
</html>
```